Luggage and travel essentials company needs Letterhead design (including logo)

Brambury luggage is a travel retailer focussed on selling luggage and travel essentials.
We are a company that have a traditional approach to customer service and also embraces the latest technology, especially where it improves the customer experience.
I would like the design to have an airport hint (airport imagery and font preferred), I would also like the colour blue to feature heavily (see attached image for colour hint).
The final design should aim to give the customer confidence that we are dependable and reliable (no script fonts or crazy colours please) but also reflect that we are an innovative and technology focused company.
I would like the letterhead design to include a logo and text.
I am interested in letterhead text containing an embedded logo (much like the 'Z' in Zephyra's logo is also used separately) Note: this is optional.
The text of the letterhead should include the words "Brambury Luggage & Travel Essentials", and should include a space for the company phone number, email address, website address along with the company physical address.
Target Market(s)
Affluent Adults aged 25 years and above - Predominantly female
Industry/Entity Type
Airport

```html
<!DOCTYPE html>
<html lang="en">
<head>
<meta charset="utf-8">
<title>Brambury Luggage &amp; Travel Essentials – Letterhead</title>
<link rel="stylesheet" href="https://fonts.googleapis.com/css2?family=Nunito+Sans:wght@400&display=swap">
<style>
  :root {
    --brand-blue: #1b93d1;
    --brand-blue-light: #7cc8ec;
    --paper: #ffffff;
    --canvas: #ffffff;
    --sheet-edge: #6d6d6d;
    --footer-text: #ffffff;
  }
  html, body {
    margin: 0;
    padding: 0;
    width: 894px;
    height: 1200px;
    overflow: hidden;
    background: var(--canvas);
    font-family: "Nunito Sans", sans-serif;
  }
  .letterhead {
    position: absolute;
    left: 62px;
    top: 37px;
    width: 781px;
    height: 1142px;
    box-sizing: border-box;
    border: 1px solid var(--sheet-edge);
    background: var(--paper);
    overflow: hidden;
  }
  .brand {
    position: absolute;
    left: 65px;
    top: 51px;
  }
  .brand-mark {
    display: block;
    width: 96px;
    height: 96px;
    background: var(--brand-blue);
    margin-bottom: 16px;
  }
  .brand-name {
    margin: 0;
    color: var(--brand-blue);
    font-size: 21px;
    font-weight: 400;
    line-height: 26px;
  }
  .footer-band {
    position: absolute;
    left: 0;
    bottom: 0;
    width: 781px;
    height: 110px;
  }
  .footer-band svg {
    position: absolute;
    inset: 0;
    display: block;
  }
  .contact {
    position: absolute;
    left: 64px;
    top: 22px;
    margin: 0;
    padding: 0;
    list-style: none;
    color: var(--footer-text);
    font-size: 10.5px;
    line-height: 13px;
  }
  .contact li { margin-bottom: 14px; }
  .website {
    position: absolute;
    right: 50px;
    top: 82px;
    margin: 0;
    color: var(--footer-text);
    font-size: 10.5px;
  }
</style>
</head>
<body>
  <main class="letterhead">
    <header class="brand">
      <span class="brand-mark" aria-hidden="true"></span>
      <p class="brand-name">Brambury Luggage<br>&amp; Travel Essentials</p>
    </header>

    <footer class="footer-band">
      <svg width="781" height="110" viewBox="0 0 781 110" aria-hidden="true">
        <polygon points="0,0 407,0 427,51 781,51 781,110 0,110" fill="var(--brand-blue-light)"/>
        <polygon points="0,8 400,8 420,59 781,59 781,110 0,110" fill="var(--brand-blue)"/>
      </svg>
      <ul class="contact">
        <li>Westbridge Shire BR4 2QT, United Kingdom</li>
        <li>Phone: +44 800 555 0147, Fax: +44 800 555 0148</li>
        <li>Email: info@bramburyluggage.example</li>
      </ul>
      <p class="website">www.bramburyluggage.example</p>
    </footer>
  </main>
</body>
</html>
```